Need Business Card for our Indian Grocery Store

Industry/Entity Type

Grocery Store

Contact Information for Business Card

Manoj Baweja
Director

Store Locations:

Northvale
482 Elm Parade
P: 03 9172 5843

Brookmere
613 Carlow Road
P: 03 9238 6014

email: kvtmarts@mailnest.example

Requirements
Must have
• Our logo Colours

```html
<!DOCTYPE html>
<html lang="en">
<head>
<meta charset="utf-8">
<title>KVT Marts – Business Card</title>
<link rel="stylesheet" href="https://fonts.googleapis.com/css2?family=Montserrat:wght@400;500;700;800&display=swap">
<style>
  :root {
    --brand-red: #e31e24;
    --paper: #ffffff;
    --ink: #3a3a3a;
    --ink-soft: #6b6b6b;
    --rule: #4a4a4a;
    --backdrop: #2b2d30;
  }
  * { box-sizing: border-box; margin: 0; padding: 0; }
  html, body {
    width: 1200px; height: 1000px; overflow: hidden;
    background: var(--backdrop);
    font-family: "Montserrat", Arial, sans-serif;
  }
  .sheet {
    position: relative; width: 1200px; height: 1000px;
    display: flex; align-items: center; justify-content: center; gap: 60px;
  }
  .card {
    position: relative; width: 520px; height: 300px;
    border-radius: 22px; overflow: hidden;
  }

  /* Front */
  .card--front { background: var(--paper); }
  .identity { position: absolute; left: 34px; top: 28px; }
  .identity__name {
    color: var(--brand-red); font-weight: 800; font-size: 20px;
    letter-spacing: 0.5px; text-transform: uppercase; line-height: 1.1;
  }
  .identity__role {
    color: var(--ink-soft); font-size: 11px; font-weight: 500;
    text-transform: uppercase; margin-top: 4px;
  }
  .identity__email { color: var(--brand-red); font-size: 13px; margin-top: 2px; }
  .identity__rule {
    position: absolute; left: 34px; top: 106px; width: 230px; height: 2px;
    background: var(--rule);
  }
  .store {
    position: absolute; display: grid; grid-template-columns: 16px auto;
    column-gap: 8px; row-gap: 3px; color: var(--ink); font-size: 14px; line-height: 1.3;
  }
  .store--north { left: 34px; top: 126px; }
  .store--south { left: 318px; top: 150px; }
  .store svg { width: 14px; height: 14px; fill: var(--brand-red); margin-top: 2px; }

  .wordmark {
    position: absolute; left: 318px; top: 78px;
    color: var(--brand-red); font-weight: 800; font-size: 28px; letter-spacing: 1px;
    line-height: 1;
  }

  .web-band {
    position: absolute; left: 0; right: 0; bottom: 0; height: 58px;
    background: var(--brand-red); color: var(--paper);
    display: flex; align-items: center; gap: 10px; padding-left: 34px;
    font-size: 16px; font-weight: 500;
  }
  .web-band svg { width: 18px; height: 18px; fill: none; stroke: var(--paper); stroke-width: 2.4; stroke-linecap: round; }

  /* Back */
  .card--back { background: var(--brand-red); display: flex; align-items: center; justify-content: center; }
  .wordmark-back {
    color: var(--paper); font-weight: 800; font-size: 44px; letter-spacing: 2px;
  }
</style>
</head>
<body>
<main class="sheet">

  <section class="card card--front" aria-label="Business card front">
    <div class="identity">
      <p class="identity__name">Manoj Baweja</p>
      <p class="identity__role">Director</p>
      <p class="identity__email">manoj@kvtmarts.example</p>
    </div>
    <div class="identity__rule"></div>

    <div class="store store--north">
      <svg viewBox="0 0 24 24"><path d="M12 2a7 7 0 0 0-7 7c0 5 7 13 7 13s7-8 7-13a7 7 0 0 0-7-7zm0 9.5A2.5 2.5 0 1 1 12 6.5a2.5 2.5 0 0 1 0 5z"/></svg>
      <span>Northvale<br>482 Elm Parade</span>
      <svg viewBox="0 0 24 24"><path d="M6.6 10.8a15 15 0 0 0 6.6 6.6l2.2-2.2a1 1 0 0 1 1-.25 11.4 11.4 0 0 0 3.6.57 1 1 0 0 1 1 1V20a1 1 0 0 1-1 1A17 17 0 0 1 3 4a1 1 0 0 1 1-1h3.5a1 1 0 0 1 1 1c0 1.25.2 2.45.57 3.57a1 1 0 0 1-.25 1z"/></svg>
      <span>03 9172 5843</span>
    </div>

    <div class="wordmark">KVT Marts</div>

    <div class="store store--south">
      <svg viewBox="0 0 24 24"><path d="M12 2a7 7 0 0 0-7 7c0 5 7 13 7 13s7-8 7-13a7 7 0 0 0-7-7zm0 9.5A2.5 2.5 0 1 1 12 6.5a2.5 2.5 0 0 1 0 5z"/></svg>
      <span>Brookmere<br>613 Carlow Road</span>
      <svg viewBox="0 0 24 24"><path d="M6.6 10.8a15 15 0 0 0 6.6 6.6l2.2-2.2a1 1 0 0 1 1-.25 11.4 11.4 0 0 0 3.6.57 1 1 0 0 1 1 1V20a1 1 0 0 1-1 1A17 17 0 0 1 3 4a1 1 0 0 1 1-1h3.5a1 1 0 0 1 1 1c0 1.25.2 2.45.57 3.57a1 1 0 0 1-.25 1z"/></svg>
      <span>03 9238 6014</span>
    </div>

    <div class="web-band">
      <svg viewBox="0 0 24 24"><path d="M10 14a4 4 0 0 0 5.7 0l3-3a4 4 0 0 0-5.7-5.7l-1.2 1.2"/><path d="M14 10a4 4 0 0 0-5.7 0l-3 3a4 4 0 0 0 5.7 5.7l1.2-1.2"/></svg>
      <span>www.kvtmarts.example</span>
    </div>
  </section>

  <section class="card card--back" aria-label="Business card back">
    <div class="wordmark-back">KVT Marts</div>
  </section>

</main>
</body>
</html>
```